Book Cover Design on Conflict resolution

I need a book cover design for the following book title. Title: "The Craft of Accord: Steering Disputes with Candor, Social Awareness, and Steadfastness" The author's name is Marcus Dellway. The book covers multiple areas to include unconscious bias, retaliation and reprisal. I am interested in seeing the designs that provide a unique eye catching presence.

Target Market(s)

Organizations and major corporations. Personal conflicts and self help. Federal Government, Schools, and Churches

Industry/Entity Type

Large Corporation, Federal Government, Churches, Schools

Font styles to use
Serif

Colors
0054AA
0677BA
7BADD7
CADEEF
E8F1F8
59FF00
82FF00
B8FF75
E3FFCB
F4FFEA

Requirements
Nice to have
• something unique and creative

```html
<!DOCTYPE html>
<html lang="en">
<head>
<meta charset="utf-8">
<title>The Craft of Accord — Book Cover</title>
<link rel="stylesheet" href="https://fonts.googleapis.com/css2?family=Saira+Extra+Condensed:wght@500;600&family=Raleway:wght@700&family=Montserrat:wght@700&display=swap">
<style>
  :root {
    --backdrop: #7a7a7a;
    --cover: #dedede;
    --ink: #111111;
    --paper: #ffffff;
    --accent-green: #4a8a4c;
    --art-teal: #2f8f86;
    --art-olive: #8c8a3a;
    --art-green: #5f9a5a;
    --art-blue: #8fb9c4;
  }
  * { margin: 0; padding: 0; box-sizing: border-box; }
  html, body {
    width: 1200px;
    height: 720px;
    overflow: hidden;
    background: var(--backdrop);
  }
  .canvas {
    position: relative;
    width: 1200px;
    height: 720px;
    display: flex;
    align-items: center;
    justify-content: center;
  }
  .book-cover {
    position: relative;
    width: 540px;
    height: 640px;
    background: var(--cover);
    overflow: hidden;
  }
  .cover-art {
    position: absolute;
    left: 230px;
    top: -40px;
    width: 340px;
    height: 340px;
    border-radius: 50%;
    background:
      linear-gradient(115deg,
        var(--art-olive) 0%, var(--art-teal) 18%, var(--art-green) 32%,
        var(--art-blue) 42%, var(--art-olive) 55%, var(--art-teal) 70%,
        var(--art-green) 85%, var(--art-teal) 100%);
  }
  .title-block {
    position: absolute;
    left: 0;
    top: 0;
    width: 540px;
    height: 640px;
    overflow: visible;
  }
  .title-lead-box { fill: var(--ink); }
  .title-lead {
    fill: var(--paper);
    font-family: "Saira Extra Condensed", "Arial Narrow", sans-serif;
    font-weight: 500;
    font-size: 54px;
  }
  .title-main {
    fill: var(--ink);
    font-family: "Saira Extra Condensed", "Arial Narrow", sans-serif;
    font-weight: 600;
    font-size: 150px;
  }
  .title-accent-dot { fill: var(--accent-green); }
  .subtitle {
    position: absolute;
    left: 52px;
    top: 552px;
    width: 440px;
    color: var(--ink);
    font-family: "Raleway", sans-serif;
    font-weight: 700;
    font-size: 15px;
    line-height: 1.25;
  }
  .author-row {
    position: absolute;
    left: 52px;
    top: 596px;
    display: flex;
    align-items: center;
    gap: 18px;
  }
  .author-name {
    color: var(--accent-green);
    font-family: "Montserrat", sans-serif;
    font-weight: 700;
    font-size: 26px;
    letter-spacing: 0.5px;
    white-space: nowrap;
  }
  .author-bar {
    width: 150px;
    height: 22px;
    background: var(--accent-green);
    margin-top: 8px;
  }
</style>
</head>
<body>
  <main class="canvas">
    <article class="book-cover">
      <div class="cover-art" role="img" aria-label="Circular hand-drawn illustration of flowing wavy bands with intricate patterns in teal, olive and green"></div>
      <h1>
        <svg class="title-block" viewBox="0 0 540 640" aria-label="The Craft of Accord">
          <rect class="title-lead-box" x="52" y="318" width="290" height="60"/>
          <text class="title-lead" x="66" y="367" textLength="262" lengthAdjust="spacingAndGlyphs">THE CRAFT OF</text>
          <circle class="title-accent-dot" cx="440" cy="382" r="24"/>
          <text class="title-main" x="48" y="540" textLength="454" lengthAdjust="spacingAndGlyphs">ACCORD</text>
        </svg>
      </h1>
      <p class="subtitle">Steering Disputes with Candor,<br>Social Awareness, and Steadfastness</p>
      <div class="author-row">
        <p class="author-name">MARCUS DELLWAY</p>
        <span class="author-bar" aria-hidden="true"></span>
      </div>
    </article>
  </main>
</body>
</html>
```